Quillory Nest Business Card

I need a business card design. We are a collaborate online training company. Our colors are gray and green. Our website is QuilloryNest.com

I would like an area for a profile picture within the card

```html
<!DOCTYPE html>
<html lang="en">
<head>
<meta charset="utf-8">
<title>Quillory Nest Business Card</title>
<link rel="stylesheet" href="https://fonts.googleapis.com/css2?family=Marcellus&family=Raleway:wght@400;500&family=Roboto+Condensed:wght@700&display=swap">
<style>
  :root {
    --page: #ffffff;
    --front-light: #fbfbfb;
    --front-shade: #d9d9d9;
    --ink: #1c1c1c;
    --brand-green: #7dbb3c;
    --back-navy: #14455f;
    --icon-red: #c0231c;
    --badge-white: #ffffff;
    --text-light: #f2f4f6;
    --divider: #b9c6cf;
    --portrait-green: #76a58a;
    --portrait-deep: #5f8f76;
  }
  * { margin: 0; padding: 0; box-sizing: border-box; }
  html, body { width: 1200px; height: 1000px; overflow: hidden; background: var(--page); }
  .canvas { position: relative; width: 1200px; height: 1000px; }

  .card { position: absolute; left: 332px; width: 521px; height: 272px; overflow: hidden; }

  /* Front */
  .card-front {
    top: 175px;
    background:
      radial-gradient(circle at 28% 45%, rgba(200,180,210,0.35), transparent 45%),
      radial-gradient(circle at 80% 30%, rgba(170,210,225,0.35), transparent 40%),
      radial-gradient(circle at 10% 25%, rgba(220,225,160,0.35), transparent 30%),
      radial-gradient(ellipse at 65% 45%, var(--front-light), var(--front-shade));
  }
  .brand {
    position: absolute; left: 14px; top: 24px;
    display: flex; align-items: center; gap: 10px;
  }
  .brand-dot { width: 34px; height: 34px; border-radius: 50%; background: var(--brand-green); }
  .brand-name {
    font-family: "Roboto Condensed", "Arial Narrow", sans-serif;
    font-weight: 700; font-size: 34px; letter-spacing: -0.5px;
    color: var(--ink); line-height: 1; white-space: nowrap;
  }
  .holder { position: absolute; left: 243px; top: 160px; width: 239px; text-align: center; }
  .holder-name {
    font-family: "Marcellus", serif; font-weight: 400; font-size: 31px; color: var(--ink);
    line-height: 1; padding-bottom: 10px; border-bottom: 1px solid var(--ink); white-space: nowrap;
  }
  .holder-role {
    font-family: "Marcellus", serif; font-size: 22px; letter-spacing: 3px;
    color: var(--ink); margin-top: 4px; white-space: nowrap;
  }

  /* Back */
  .card-back {
    top: 528px;
    background:
      radial-gradient(circle at 45% 35%, rgba(130,80,120,0.45), transparent 30%),
      radial-gradient(circle at 92% 20%, rgba(140,160,90,0.5), transparent 22%),
      radial-gradient(circle at 60% 10%, rgba(60,140,170,0.5), transparent 30%),
      var(--back-navy);
  }
  .contact-list { position: absolute; left: 22px; top: 36px; width: 250px; height: 190px; list-style: none; }
  .contact-item { position: absolute; left: 0; width: 250px; display: flex; align-items: flex-start; }
  .contact-address { top: 0; }
  .contact-web { top: 68px; }
  .contact-phone { top: 146px; }
  .badge {
    width: 46px; height: 46px; border-radius: 50%; background: var(--badge-white);
    display: flex; align-items: center; justify-content: center; flex: none; margin-top: 6px;
  }
  .badge svg { width: 28px; height: 28px; }
  .contact-text { margin-left: 10px; color: var(--text-light); white-space: nowrap; }
  .contact-label { font-family: "Raleway", sans-serif; font-size: 11.5px; line-height: 14px; }
  .contact-value { font-family: "Raleway", sans-serif; font-weight: 500; font-size: 13.5px; line-height: 18px; }
  .contact-gap { margin-top: 5px; }
  .divider { position: absolute; left: 277px; top: 47px; width: 1px; height: 180px; background: var(--divider); }
  .portrait {
    position: absolute; left: 305px; top: 43px; width: 186px; height: 185px;
    background: linear-gradient(135deg, var(--portrait-green), var(--portrait-deep));
  }
</style>
</head>
<body>
<main class="canvas">
  <section class="card card-front" aria-label="Business card front">
    <div class="brand">
      <span class="brand-dot"></span>
      <span class="brand-name">Quillory Nest</span>
    </div>
    <div class="holder">
      <h1 class="holder-name">Mara Lindqvist</h1>
      <p class="holder-role">HRD Manager</p>
    </div>
  </section>

  <section class="card card-back" aria-label="Business card back">
    <ul class="contact-list">
      <li class="contact-item contact-address">
        <span class="badge">
          <svg viewBox="0 0 28 28" fill="none" stroke="var(--icon-red)" stroke-width="2.4" stroke-linejoin="round">
            <path d="M3 14 L14 4 L25 14"/>
            <path d="M6.5 12 V24 H21.5 V12"/>
            <rect x="11.5" y="15" width="5" height="5" fill="var(--icon-red)" stroke="none"/>
          </svg>
        </span>
        <div class="contact-text">
          <p class="contact-label">Address:</p>
          <p class="contact-value">412 Alder Lane</p>
          <p class="contact-value">Riverton, OR. 974120</p>
        </div>
      </li>
      <li class="contact-item contact-web">
        <span class="badge">
          <svg viewBox="0 0 28 28" fill="none" stroke="var(--icon-red)" stroke-width="1.8">
            <circle cx="14" cy="14" r="11"/>
            <ellipse cx="14" cy="14" rx="5" ry="11"/>
            <path d="M3 14 H25 M5 8 H23 M5 20 H23"/>
          </svg>
        </span>
        <div class="contact-text">
          <p class="contact-label">Website:</p>
          <p class="contact-value">maralindqvist.com</p>
          <p class="contact-label contact-gap">Email:</p>
          <p class="contact-value">mara@quillorynest.com</p>
        </div>
      </li>
      <li class="contact-item contact-phone">
        <span class="badge">
          <svg viewBox="0 0 28 28">
            <path fill="var(--icon-red)" d="M7 4 L11 8.5 L8.8 11 C10.3 14.3 13.7 17.7 17 19.2 L19.5 17 L24 21 L21.5 24.5 C13 24 4 15 3.5 6.5 Z"/>
          </svg>
        </span>
        <div class="contact-text">
          <p class="contact-label">Phone:</p>
          <p class="contact-value">(503) 214-6093</p>
        </div>
      </li>
    </ul>
    <div class="divider"></div>
    <div class="portrait" role="img" aria-label="Profile picture area for the card holder"></div>
  </section>
</main>
</body>
</html>
```